Transform Your Giving

I need a tri-fold brochure that will fit in a standard number 10 business envelope. Harborline and Caring Works is a charitable nonprofit. The goal of this brochure is to stimulate people into thinking about other ways to make a donation. The design should communicate the essential information on donation options, create a sense of professional integrity, be graphically sharp, easy to read and laid out in a way that doesn't make the material appear crowded.

```html
<!DOCTYPE html>
<html lang="en">
<head>
<meta charset="utf-8">
<title>Transform Your Giving – Harborline and Caring Works</title>
<link rel="stylesheet" href="https://fonts.googleapis.com/css2?family=Barlow:ital,wght@0,600;0,700;0,800;1,600;1,700&family=Figtree:ital,wght@0,400;0,500;0,600;0,700;1,400&display=swap">
<style>
:root{
  --navy:#29236f;
  --green:#4cb848;
  --ink:#1f1f2a;
  --stage:#767676;
  --paper:#ffffff;
  --grey-mark:#a8a8ad;
}
*{box-sizing:border-box;margin:0;padding:0}
html,body{width:1096px;height:1200px;overflow:hidden;background:var(--stage)}
body{position:relative;font-family:"Figtree",sans-serif;color:var(--ink)}
.spread{position:absolute;left:205px;width:687px;height:515px;display:flex}
.spread--outside{top:63px}
.spread--inside{top:621px}
.panel{position:relative;width:229px;height:515px;background:var(--paper);overflow:hidden}
.panel--navy{background:var(--navy);color:#fff}
.panel--fold-left{box-shadow:inset -10px 0 12px -10px rgba(0,0,0,.18)}
.panel--fold-right{box-shadow:inset 10px 0 12px -10px rgba(0,0,0,.18)}
.photo{position:absolute;left:0;width:229px}
.curve{position:absolute;left:0;width:229px;height:34px}
.heading{font-family:"Barlow",sans-serif;font-weight:800;color:var(--navy)}
.tagline{font-family:"Barlow",sans-serif;font-style:italic;font-weight:700;color:var(--green)}
.wordmark{font-family:"Barlow",sans-serif;font-weight:800;text-align:center;letter-spacing:1px}
.wordmark small{display:block;font-size:5px;letter-spacing:.6px;font-weight:700;margin-top:1px}

/* outside, panel 1 */
.impact{position:absolute;left:18px;top:276px;width:200px}
.impact h2{font-size:12.5px;letter-spacing:.2px}
.impact p{font-size:9.6px;line-height:12.9px;margin-top:2px;color:#222}
.checklist{list-style:none;display:grid;grid-template-columns:58px 1fr;row-gap:6px;margin-top:13px;font-family:"Barlow",sans-serif;font-weight:600;font-size:10.5px;color:#1a1a1a}
.checklist li{display:flex;align-items:center;gap:6px}
.tick{width:8px;height:8px;flex:none}
.impact-mark{position:absolute;left:95px;top:455px;width:120px;color:var(--grey-mark);font-size:24px}

/* outside, panel 2 */
.contact-intro{position:absolute;left:14px;top:17px;width:201px;text-align:center;font-size:8.6px;font-weight:600;line-height:11.5px}
.quote{position:absolute;z-index:2;left:14px;top:92px;width:201px;text-align:center;font-size:8.6px;font-style:italic;line-height:11.5px;color:#e6e5f3}
.will{position:absolute;left:8px;top:225px;width:213px;text-align:center;font-size:8.6px;line-height:11px}
.will a{color:var(--green);text-decoration:underline}
.contact-mark{position:absolute;left:40px;top:270px;width:150px;font-size:30px;color:#fff}
.contact-mark small{color:#fff}
.contact{position:absolute;left:10px;top:338px;width:209px;text-align:center}
.contact h3{font-family:"Barlow",sans-serif;font-weight:800;font-size:11px;text-decoration:underline}
.contact .lead{color:var(--green);font-weight:700;font-size:8.4px;line-height:11.5px;margin-top:4px}
.contact-item{font-size:8px;line-height:10.5px;margin-top:3px}
.contact-item svg{display:block;margin:0 auto 2px;width:8px;height:8px}
.follow{margin-top:5px;display:flex;justify-content:center;align-items:center;gap:3px;font-family:"Barlow",sans-serif;font-weight:800;font-size:9px}
.follow span{text-decoration:underline;margin-right:2px}
.follow i{width:9px;height:9px;border-radius:50%;background:var(--green);display:inline-block}

/* outside, panel 3 (cover) */
.cover-title{position:absolute;left:0;top:13px;width:229px;text-align:center;font-family:"Barlow",sans-serif;font-weight:800;font-size:18.5px;line-height:20px}
.cover-title .navy{color:var(--navy)}
.cover-title .green{color:var(--green)}
.cover-sub{position:absolute;left:20px;top:57px;width:189px;text-align:center;font-family:"Barlow",sans-serif;font-weight:700;font-size:9px;line-height:11.5px;color:var(--navy)}
.options{position:absolute;left:0;width:229px}
.option{position:absolute;text-align:center;font-family:"Barlow",sans-serif;font-weight:700;font-size:10.5px;line-height:12.5px;color:#1a1a1a;width:70px}
.option svg{display:block;margin:0 auto 5px;width:42px;height:42px}
.dots{position:absolute;height:0;border-top:1.5px dotted var(--navy)}
.cover-mark{position:absolute;left:20px;top:452px;width:189px;font-size:36px;color:var(--navy)}
.cover-mark small{color:var(--navy);font-size:6px}

/* inside */
.inside-copy{position:absolute;left:18px;width:200px}
.intro{top:16px;font-size:8.6px;line-height:11.4px;font-weight:500}
.feature{display:grid;grid-template-columns:56px 1fr;align-items:start}
.feature svg{width:51px;height:51px}
.feature h3{font-family:"Barlow",sans-serif;font-weight:700;font-size:9.6px;line-height:11.5px;color:var(--navy)}
.feature .tagline{font-size:9px;line-height:11.2px;margin-top:2px}
.body{font-size:8.3px;line-height:10.9px;color:#2a2a2a}
.how{font-family:"Barlow",sans-serif;font-weight:700;font-size:10.8px;color:var(--navy);margin-top:7px}
.benefits{list-style:none;margin:7px 0 0 0}
.benefits li{display:grid;grid-template-columns:10px 1fr;font-size:8px;line-height:10.3px;margin-bottom:6px}
.benefits .tick{margin-top:1px}
</style>
</head>
<body>

<svg width="0" height="0" style="position:absolute" aria-hidden="true">
  <defs>
    <symbol id="ring" viewBox="0 0 50 50"><circle cx="25" cy="25" r="23.5" fill="var(--navy)" stroke="var(--green)" stroke-width="2.5"/><circle cx="25" cy="25" r="20.5" fill="none" stroke="#fff" stroke-width="1.5"/></symbol>
    <symbol id="icon-coin" viewBox="0 0 50 50"><use href="#ring"/><circle cx="25" cy="25" r="10" fill="none" stroke="#fff" stroke-width="1.6"/><circle cx="25" cy="25" r="6" fill="none" stroke="#fff" stroke-width="1.2"/></symbol>
    <symbol id="icon-bank" viewBox="0 0 50 50"><use href="#ring"/><g fill="none" stroke="#fff" stroke-width="1.5"><path d="M14 20 L25 13 L36 20 Z"/><path d="M14 35 H36 M15 32 H35"/><path d="M18 22 V30 M22 22 V30 M28 22 V30 M32 22 V30"/></g></symbol>
    <symbol id="icon-gift" viewBox="0 0 50 50"><use href="#ring"/><g fill="none" stroke="#fff" stroke-width="1.5"><rect x="15" y="20" width="20" height="5"/><rect x="16.5" y="25" width="17" height="11"/><path d="M25 20 V36"/><path d="M25 20 C21 13 15 16 20 20 M25 20 C29 13 35 16 30 20"/></g></symbol>
    <symbol id="icon-chart" viewBox="0 0 50 50"><use href="#ring"/><g fill="none" stroke="#fff" stroke-width="1.5"><path d="M13 36 H37"/><rect x="16" y="28" width="4" height="8"/><rect x="22" y="24" width="4" height="12"/><rect x="28" y="20" width="4" height="16"/><path d="M15 25 L34 14 M30 13.5 L34 14 L33 17.5"/></g></symbol>
    <symbol id="icon-calendar" viewBox="0 0 50 50"><use href="#ring"/><g fill="none" stroke="#fff" stroke-width="1.4"><rect x="14" y="17" width="22" height="19" rx="1.5"/><path d="M14 22 H36 M19 14 V19 M31 14 V19"/><circle cx="25" cy="16" r="3.5"/><path d="M18 26 h3 M23.5 26 h3 M29 26 h3 M18 31 h3 M23.5 31 h3 M29 31 h3"/></g></symbol>
    <symbol id="tick" viewBox="0 0 10 10"><circle cx="5" cy="5" r="5" fill="var(--navy)"/><path d="M2.8 5.1 L4.4 6.6 L7.3 3.6" fill="none" stroke="#fff" stroke-width="1.3"/></symbol>
    <symbol id="arc-white" viewBox="0 0 229 34" preserveAspectRatio="none"><path d="M0 34 V30 Q114 -6 229 30 V34 Z" fill="#fff"/><path d="M0 30 Q114 -6 229 30" fill="none" stroke="var(--green)" stroke-width="4"/></symbol>
  </defs>
</svg>

<!-- Outside spread -->
<section class="spread spread--outside">

  <article class="panel panel--fold-left">
    <svg class="photo" style="top:0;height:264px" role="img" aria-label="Photo of a young woman holding hands with an elderly woman outdoors among green trees">
      <defs><linearGradient id="g-park" x1="0" y1="0" x2="0" y2="1"><stop offset="0" stop-color="#6f9a3e"/><stop offset=".5" stop-color="#5a7f3a"/><stop offset="1" stop-color="#2f4a7a"/></linearGradient></defs>
      <rect width="229" height="264" fill="url(#g-park)"/>
    </svg>
    <svg class="curve" style="top:232px"><use href="#arc-white"/></svg>
    <div class="impact">
      <h2 class="heading">THE IMPACT OF YOUR GIFT</h2>
      <p>Your generosity drives our mission. With every Smart gift you’re supporting Harborline and Caring Works. Join our community of Smart Givers today and make an enduring impact. With Smart Giving your generosity reaches further.&nbsp; Begin your Smart Giving journey with us today.</p>
      <ul class="checklist">
        <li><svg class="tick"><use href="#tick"/></svg>DAFs</li>
        <li><svg class="tick"><use href="#tick"/></svg>Stocks and Securities</li>
        <li><svg class="tick"><use href="#tick"/></svg>QCDs</li>
        <li><svg class="tick"><use href="#tick"/></svg>Charitable Annuity</li>
        <li><svg class="tick"><use href="#tick"/></svg>Crypto</li>
      </ul>
    </div>
    <div class="wordmark impact-mark">HCW<small>HARBORLINE AND CARING WORKS</small></div>
  </article>

  <article class="panel panel--navy">
    <p class="contact-intro">To learn more about Smart Giving Options and how they can benefit you and Harborline and Caring Works, please reach out to our team.&nbsp; We’re here to help you navigate these giving methods and answer any question you may have.</p>
    <p class="quote">Being kind to others is a way of<br>being good to yourself.<br>Miriam Ashcombe</p>
    <svg class="photo" style="top:98px;height:122px" role="img" aria-label="Close-up of a younger hand gently holding an elderly hand">
      <defs><linearGradient id="g-hands" x1="0" y1="0" x2="1" y2="0"><stop offset="0" stop-color="#e8845a"/><stop offset=".55" stop-color="#f2b28a"/><stop offset="1" stop-color="#29236f" stop-opacity="0"/></linearGradient></defs>
      <path d="M0 78 Q90 50 229 34 V80 Q120 100 0 122 Z" fill="url(#g-hands)"/>
    </svg>
    <p class="will">If you do not have a will, go to<br><a>www.EasyWillNow.org</a><br>In 20 minutes you can have a legal will – for free.</p>
    <div class="wordmark contact-mark">HCW<small>HARBORLINE AND CARING WORKS</small></div>
    <div class="contact">
      <h3>CONTACT US</h3>
      <p class="lead">Have more question? Please contact us at<br>Harborline and Caring Works</p>
      <p class="contact-item"><svg viewBox="0 0 10 10"><circle cx="5" cy="5" r="5" fill="var(--green)"/><path d="M5 2.2a1.8 1.8 0 0 1 1.8 1.8C6.8 5.4 5 7.6 5 7.6S3.2 5.4 3.2 4A1.8 1.8 0 0 1 5 2.2z" fill="var(--navy)"/></svg>1420 Cedarline Ave.<br>Suite 4 Marlow, ND&nbsp; 58511</p>
      <p class="contact-item"><svg viewBox="0 0 10 10"><circle cx="5" cy="5" r="5" fill="var(--green)"/><path d="M3 2.5 L4.2 2.3 L4.7 3.8 L4 4.3 Q4.6 5.6 5.8 6.1 L6.3 5.4 L7.7 5.9 L7.5 7.1 Q4 7.3 3 2.5z" fill="var(--navy)"/></svg>701-555-0142 (ext. 100)</p>
      <p class="contact-item"><svg viewBox="0 0 10 10"><circle cx="5" cy="5" r="5" fill="var(--green)"/><rect x="2.6" y="3.3" width="4.8" height="3.4" fill="var(--navy)"/><path d="M2.6 3.3 L5 5.2 L7.4 3.3" fill="none" stroke="var(--green)" stroke-width=".6"/></svg>jmoreau@harborlinecw.org</p>
      <p class="contact-item"><svg viewBox="0 0 10 10"><circle cx="5" cy="5" r="5" fill="var(--green)"/><circle cx="5" cy="5" r="2.6" fill="none" stroke="var(--navy)" stroke-width=".7"/><path d="M2.4 5 H7.6 M5 2.4 V7.6" stroke="var(--navy)" stroke-width=".6"/></svg>www.harborlinecw.org</p>
      <p class="follow"><span>FOLLOW US:</span><i></i><i></i></p>
    </div>
  </article>

  <article class="panel">
    <h1 class="cover-title"><span class="navy">Transform Your Giving</span><br><span class="green">Be Strategic, Be Smart</span></h1>
    <p class="cover-sub">Discover the impact of Smart Giving with Harborline and Caring Works</p>
    <svg class="photo" style="top:92px;height:200px" role="img" aria-label="Photo of an older man and a younger man smiling and clasping hands at home">
      <defs><linearGradient id="g-home" x1="0" y1="0" x2="1" y2="1"><stop offset="0" stop-color="#c9c4bc"/><stop offset=".5" stop-color="#a07a50"/><stop offset="1" stop-color="#3f5c82"/></linearGradient></defs>
      <rect width="229" height="200" fill="url(#g-home)"/>
    </svg>
    <svg class="curve" style="top:84px;transform:scaleY(-1)"><use href="#arc-white"/></svg>
    <svg class="curve" style="top:262px"><use href="#arc-white"/></svg>
    <div class="options" style="top:0">
      <div class="dots" style="left:70px;top:310px;width:30px"></div>
      <div class="dots" style="left:138px;top:310px;width:26px"></div>
      <div class="dots" style="left:105px;top:369px;width:28px"></div>
      <div class="option" style="left:0;top:288px"><svg><use href="#icon-coin"/></svg>CRYPTO</div>
      <div class="option" style="left:69px;top:288px"><svg><use href="#icon-bank"/></svg>DAF’S</div>
      <div class="option" style="left:153px;top:288px"><svg><use href="#icon-gift"/></svg>QCDS</div>
      <div class="option" style="left:31px;top:348px"><svg><use href="#icon-chart"/></svg>STOCKS &amp;<br>SECURITIES</div>
      <div class="option" style="left:109px;top:348px"><svg><use href="#icon-calendar"/></svg>CHARITABLE<br>ANNUITY</div>
    </div>
    <div class="wordmark cover-mark">HCW<small>HARBORLINE AND CARING WORKS</small></div>
  </article>
</section>

<!-- Inside spread -->
<section class="spread spread--inside">

  <article class="panel panel--fold-left">
    <p class="inside-copy intro">We would like to introduce you to five Strategic and Smart ways to give that could potentially be more beneficial to you compared to traditional cash donations. We encourage you to keep this information as a guide for your future contributions.</p>
    <div class="inside-copy" style="top:90px">
      <div class="feature"><svg><use href="#icon-chart"/></svg><div><h3>Gifts of Stocks or Appreciated Assets Strategic &amp; Smart</h3><p class="tagline">Consider your long-term publicly traded stock as a way to give to your favorite charity.</p></div></div>
      <p class="body" style="margin-top:4px">You can make a significantly bigger impact when you donate long-term appreciated securities, including stock, mutual funds, &amp; bonds, directly to your favorite charity.</p>
      <p class="how">How Does It Work?</p>
      <p class="body">When you donate stock to a charity, you will generally take a tax deduction for the full market value. Because you are donating stock, your contribution &amp; tax deduction may be significantly higher than contributing the after-tax proceeds. The same benefits apply when you donate mutual funds or bonds.</p>
    </div>
    <div class="inside-copy" style="top:313px">
      <div class="feature"><svg><use href="#icon-bank"/></svg><div><h3>Donor-Advised Fund (DAF)<br>Strategic &amp; Smart</h3><p class="tagline">Consider a DAF – a simple, flexible, and tax-advantageous way to give to your favorite charities.</p></div></div>
      <p class="body" style="margin-top:3px">A Donor-Advised Fund (DAF), is like a charitable investment account for the sole purpose of supporting your favorite charities.</p>
      <p class="how">How Does It Work?</p>
      <p class="body">You establish a DAF &amp; contribute cash, stocks, or non-publicly traded assets, cryptocurrency, &amp; private company stock to be eligible for an immediate tax deduction. Those funds are contributed for tax-free growth. You can recommend grants be made from your DAF to any IRS qualified public charity.</p>
    </div>
  </article>

  <article class="panel panel--fold-right">
    <div class="inside-copy" style="top:18px">
      <div class="feature"><svg><use href="#icon-gift"/></svg><div><h3>Qualified Charitable Distributions (QCDs) Strategic &amp; Smart</h3><p class="tagline">Consider a QCD – when planning your IRA withdrawal strategy... &amp; donate to your favorite charity.</p></div></div>
      <p class="body" style="margin-top:4px">IRA owners at age 70 ½ or over can transfer dollars from their IRA to charity tax-free each year. These transfers known as Qualified Charitable Distributions (QCDs) offer eligible older Americans a great way to easily give to charity.</p>
      <p class="how">How Does It Work?</p>
      <p class="body">Are you 72 and required to take a minimum distribution (RMD) from your IRA but do not need the funds? Consider a Qualified Charitable Distribution. Normally, distributions from a traditional IRA are taxable when received. With a QCD, these distributions become tax-free when paid directly from the IRA to your favorite eligible charity. An IRA owner wishing to make a QCD should contact their IRA trustee, allowing time to complete the transaction before the end of the year to receive the tax benefit.</p>
    </div>
    <div class="inside-copy" style="top:293px">
      <div class="feature"><svg><use href="#icon-calendar"/></svg><div><h3>Charitable Gift Annuity<br>Strategic &amp; Smart</h3><p class="tagline">Consider establishing a Charitable Gift Annuity</p></div></div>
      <p class="body" style="margin-top:6px">You make a donation to a single charity. The gift is set aside in a reserve account and invested.</p>
      <p class="how">How Does It Work?</p>
      <p class="body">A charitable gift annuity is a contract between a donor &amp; a charity. As a donor, you make a sizable gift to charity using cash, securities, or possibly other assets. This money is then invested. In return, you become eligible to take a partial tax deduction for your donation, plus you receive a fixed stream of income from the charity for the rest of your life. At the end of your life (as well as your spouse’s, if you’re giving as a couple), the charity receives the remainder of the gift.</p>
    </div>
  </article>

  <article class="panel">
    <div class="inside-copy" style="top:17px;left:16px;width:203px">
      <div class="feature"><svg><use href="#icon-coin"/></svg><div><h3 style="font-size:10.5px;line-height:12.5px">Cryptocurrency<br>Strategic &amp; Smart</h3><p class="tagline">Consider donating Bitcoin and other cryptocurrencies to your favorite charity.</p></div></div>
      <p class="body" style="font-size:9.2px;line-height:12px;margin-top:4px">Bitcoin and other cryptocurrencies can be donated to charity just like other appreciated assets such as stocks and other business interests. Before you sell bitcoin &amp; donate the after-tax proceeds, consider donating your bitcoin directly to a favorite charity.</p>
      <p class="how">How Does It Work?</p>
      <p class="body">Many donors find it useful to open a Donor-Advised Fund (DAF). This strategy includes two significant benefits, both for you and your favorite charity.</p>
      <ul class="benefits">
        <li><svg class="tick"><use href="#tick"/></svg><span>Your tax deduction will be equal to the fair market value of the donated bitcoin (as determined by a qualified appraisal).</span></li>
        <li><svg class="tick"><use href="#tick"/></svg><span>Your cryptocurrency donation is tax-smart because it may eliminate capital gains taxes on the value / appreciation AND your favorite charity will receive 100% of the value of the contribution.</span></li>
      </ul>
      <p class="body">Often charities are not able to accept direct donations of bitcoin/crypto so using a DAF is a great way to donate these assets.</p>
    </div>
    <svg class="photo" style="top:368px;height:147px" role="img" aria-label="Soft-focus photo of two pairs of hands, young and elderly, held together">
      <defs><linearGradient id="g-care" x1="0" y1="0" x2="1" y2="1"><stop offset="0" stop-color="#9aa3b3"/><stop offset=".5" stop-color="#d9b7a0"/><stop offset="1" stop-color="#5c6577"/></linearGradient></defs>
      <rect width="229" height="147" fill="url(#g-care)"/>
    </svg>
    <svg class="curve" style="top:360px;transform:scaleY(-1)"><use href="#arc-white"/></svg>
  </article>
</section>

</body>
</html>
```